Redesign Business Cards, Attached

Please read instructions carefully. If you have any questions send a message before submitting your ONE design. Please redesign attached business cards. Double sided. Use same content and descriptions. Use black, silver, crimson red and gold colors. My only issue with the attached design is the background colors. I like the layout as-is. I can provide the individual pictures on the back side later. Do not submit more than one design. One submission shall include both front and back. Do not submit front and back separately. A second project will be launched to create a matching post card after completion of this.
Industry/Entity Type
see description and attachments.
Contact Information for Business Card
Requirements
Must have
- see description and attachments.
Nice to have
Should not have

```html
<!DOCTYPE html>
<html lang="en">
<head>
<meta charset="utf-8">
<title>Helm Ready Boat Training – Business Card</title>
<link rel="stylesheet" href="https://fonts.googleapis.com/css2?family=Poppins:ital,wght@0,300;0,400;0,600;0,700;0,800;1,600;1,700&display=swap">
<style>
  :root{
    --stage:#58595b;
    --black:#1c1c1c;
    --charcoal:#3a3a3a;
    --crimson:#a00000;
    --gold-dark:#b8862a;
    --gold-light:#f2cf72;
    --silver-1:#c9c9cb;
    --silver-2:#f4f4f5;
    --ink:#3d3d3d;
    --white:#ffffff;
  }
  *{box-sizing:border-box;margin:0;padding:0}
  html,body{width:1200px;height:1200px;overflow:hidden}
  body{background:var(--stage);font-family:"Poppins",sans-serif;position:relative}
  .card{position:absolute;left:235px;width:730px;height:418px;overflow:hidden;background:var(--black)}
  .card--front{top:138px}
  .card--back{top:644px}
  .water{position:absolute;inset:0;background:radial-gradient(ellipse at 30% 40%,#3c3c3c 0%,#262626 55%,#151515 100%)}
  .shapes{position:absolute;inset:0;width:730px;height:418px}
  .brand{position:absolute;border-radius:50%;background:var(--white);display:flex;align-items:center;justify-content:center;text-align:center;color:var(--black);font-weight:700;line-height:1.2}
  .brand--front{left:52px;top:110px;width:198px;height:198px;font-size:20px}
  .brand--back{left:120px;top:25px;width:138px;height:138px;font-size:14px}
  .contact{position:absolute;left:412px;top:0;color:var(--ink)}
  .contact__name{position:absolute;top:96px;white-space:nowrap;font-size:29px;font-weight:800;color:var(--crimson);letter-spacing:.2px}
  .contact__role{position:absolute;top:134px;white-space:nowrap;font-size:20.5px;font-weight:300;line-height:25px}
  .contact__phone{position:absolute;top:219px;width:274px;height:42px;border-radius:7px;background:var(--crimson);color:var(--white);display:flex;align-items:center;justify-content:center;gap:10px;font-size:22px;font-weight:700;white-space:nowrap}
  .contact__line{position:absolute;left:0;display:flex;align-items:center;gap:11px;font-size:19px;font-weight:400;white-space:nowrap}
  .contact__line--mail{top:274px}
  .contact__line--web{top:306px}
  .icon{width:22px;height:22px;border-radius:50%;background:var(--charcoal);display:flex;align-items:center;justify-content:center}
  .boat-photo{position:absolute;inset:0;background:linear-gradient(135deg,#6a6a6a 0%,#b5b5b5 45%,#e8e8e8 70%,#8a8a8a 100%);clip-path:polygon(418px 0,730px 0,730px 236px,674px 236px,690px 182px,402px 182px,352px 95px)}
  .service{position:absolute;width:138px;height:82px;display:flex;align-items:center;justify-content:center;text-align:center;font-style:italic;font-weight:600;font-size:14px;line-height:17px;clip-path:polygon(25px 0,100% 0,calc(100% - 25px) 100%,0 100%);padding:0 18px}
  .service--gold{background:linear-gradient(90deg,var(--gold-dark),var(--gold-light) 55%,var(--gold-dark));color:var(--black)}
  .service--red{background:var(--crimson);color:var(--white)}
  .back-url{position:absolute;left:0;right:0;top:375px;text-align:center;font-size:18px;font-weight:600;color:#d4d4d4}
</style>
</head>
<body>

<section class="card card--front">
  <div class="water" role="img" aria-label="Dark black and white photo of open water"></div>
  <svg class="shapes" viewBox="0 0 730 418" aria-hidden="true">
    <defs>
      <linearGradient id="silver" x1="0" y1="0" x2="1" y2="0.3">
        <stop offset="0" stop-color="var(--silver-1)"/>
        <stop offset="0.55" stop-color="var(--silver-2)"/>
        <stop offset="1" stop-color="#b3b3b6"/>
      </linearGradient>
      <linearGradient id="gold" x1="0" y1="0" x2="0" y2="1">
        <stop offset="0" stop-color="var(--gold-light)"/>
        <stop offset="0.5" stop-color="var(--gold-dark)"/>
        <stop offset="1" stop-color="var(--gold-light)"/>
      </linearGradient>
    </defs>
    <polygon points="371,0 410,0 355,100 332,66" fill="var(--crimson)"/>
    <polygon points="332,352 355,318 410,418 371,418" fill="var(--crimson)"/>
    <polygon points="417,0 730,0 730,418 417,418 305,209" fill="url(#silver)"/>
    <polygon points="405,0 417,0 305,209 417,418 405,418 292,209" fill="url(#gold)"/>
  </svg>
  <div class="brand brand--front">Helm Ready<br>Boat Training</div>
  <div class="contact">
    <div class="contact__name">DANA R. WHITLOCK</div>
    <div class="contact__role">USGC Licensed Captain<br>Certified Instructor</div>
    <div class="contact__phone">TEXT
      <svg width="20" height="20" viewBox="0 0 24 24" aria-hidden="true"><path fill="#fff" d="M6.6 10.8a15 15 0 0 0 6.6 6.6l2.2-2.2c.3-.3.7-.4 1-.2 1.1.4 2.3.6 3.6.6.6 0 1 .4 1 1V20c0 .6-.4 1-1 1A17 17 0 0 1 3 4c0-.6.4-1 1-1h3.5c.6 0 1 .4 1 1 0 1.3.2 2.5.6 3.6.1.3 0 .7-.2 1z"/></svg>
      (555) 014-2260</div>
    <div class="contact__line contact__line--mail">
      <span class="icon"><svg width="12" height="10" viewBox="0 0 12 10" aria-hidden="true"><rect x="0.8" y="0.8" width="10.4" height="8.4" rx="1" fill="none" stroke="#fff" stroke-width="1.5"/><path d="M1 1.5 6 5.5 11 1.5" fill="none" stroke="#fff" stroke-width="1.5"/></svg></span>
      hello@helmready.com</div>
    <div class="contact__line contact__line--web">
      <span class="icon"><svg width="14" height="14" viewBox="0 0 14 14" aria-hidden="true"><g fill="none" stroke="#fff" stroke-width="1.1"><circle cx="7" cy="7" r="6"/><ellipse cx="7" cy="7" rx="2.6" ry="6"/><path d="M1 7h12M2 4h10M2 10h10"/></g></svg></span>
      www.HelmReady.com</div>
  </div>
</section>

<section class="card card--back">
  <div class="water" role="img" aria-label="Dark black and white photo of open water"></div>
  <div class="boat-photo" role="img" aria-label="Black and white photo of a center console boat cruising on sparkling water"></div>
  <svg class="shapes" viewBox="0 0 730 418" aria-hidden="true">
    <defs>
      <linearGradient id="goldBack" x1="0" y1="0" x2="0" y2="1">
        <stop offset="0" stop-color="var(--gold-light)"/>
        <stop offset="0.5" stop-color="var(--gold-dark)"/>
        <stop offset="1" stop-color="var(--gold-light)"/>
      </linearGradient>
    </defs>
    <polygon points="405,0 415,0 356,95 408,182 398,182 346,95" fill="url(#goldBack)"/>
  </svg>
  <div class="brand brand--back">Helm Ready<br>Boat Training</div>

  <div class="service service--gold" style="left:83px;top:189px">Hands-On Boat Training</div>
  <div class="service service--red" style="left:228px;top:189px">Introduction to Power Boating</div>
  <div class="service service--gold" style="left:372px;top:189px">Precision Docking and Boat Handling</div>
  <div class="service service--red" style="left:517px;top:189px">Open Water Boat Handling</div>

  <div class="service service--red" style="left:55px;top:279px">Island Anchoring</div>
  <div class="service service--gold" style="left:200px;top:279px">Open Water Advanced Maneuvers</div>
  <div class="service service--red" style="left:344px;top:279px">Coastal Navigation</div>
  <div class="service service--gold" style="left:489px;top:279px">Captaining/ Piloting Service for Your Outings</div>

  <div class="back-url">www.HelmReady.com</div>
</section>

</body>
</html>
```